Poster for Billard- & Sportsbar: "Specials"

Hi,
I Need a Poster for my Billard- & Sportsbar, which Shows our weekly Specials.
The size should be DinA0 (84 x 118.8 cm). Please notice the print instructions attached.

Text Information for the Poster:

"Wochenhighlights

Dienstag: Flatrate-Billard
Für nur 5€ (7€) pro Person den ganzen Abend Pool-Billard (Snooker)spielen

Mittwoch: Studenten-Nacht
Studenten & Auszubildende spielen Pool-Billard für nur 4,50€ die Stunde

Donnerstag: Snooker-Donnerstag
Donnerstags kostet der Snooker Tisch gerade mal 5€ die Stunde

Freitag: Kesselgold-Special
6 Talhof Kesselgold-Pils für nur 11,99€

Samstag: Schau dein Wunschsspiel
Reserviere die Private Lounge und schaue das Staffelrunde-Spiel deiner Wahl. Reservierungsgebühr: 10€, ab 6 Personen kostenlos.
(Gilt auch für EP, VKT-Pokal & Englische Wochen)

Sonntag: Play for Free
Wer vor 18:00 Uhr mit dem Spielen beginnt, spielt den ganzen Abend umsonst!"

You can choose the Colors free. If you use Pictures, take care that they are free or send me the link where they can get bought.

I have uploaded the logo of my bar. You can use it in the poster, but please not too big.

You can maybe use the Colors of the logo as main Colors. But it is not a must.

If you have questions, just contact me!

Thank you in advance!

Jorik

A short update: Please mind, that it is the most important Thing, that the customers can read the Special offers! Thank you

```html
<!DOCTYPE html>
<html lang="de">
<head>
<meta charset="utf-8">
<title>Wochenhighlights – Kugelwerk</title>
<link rel="stylesheet" href="https://fonts.googleapis.com/css2?family=Archivo+Black&family=Arimo:wght@700&display=swap">
<style>
  :root {
    --bg-deep: #2a1208;
    --bg-warm: #7a3a12;
    --amber: #f0a52a;
    --panel: rgba(38, 30, 28, 0.92);
    --mint: #7fe6cf;
    --price: #f6b02c;
    --title: #3a3434;
    --brand: #3f8f86;
  }
  * { margin: 0; padding: 0; box-sizing: border-box; }
  html, body { width: 872px; height: 1200px; overflow: hidden; }
  body { background: var(--bg-deep); font-family: "Arimo", Arial, sans-serif; font-weight: 700; }
  .poster {
    position: relative; width: 872px; height: 1200px; overflow: hidden;
    background:
      radial-gradient(ellipse 60% 22% at 50% 40%, rgba(255,244,220,0.95), rgba(255,220,160,0.5) 45%, transparent 75%),
      linear-gradient(180deg, var(--bg-warm) 0%, #b8672a 36%, #e8b37a 43%, #8a4a1c 62%, #4a200c 80%, var(--bg-deep) 100%);
  }
  .hero-photo {
    position: absolute; left: 0; top: 0; width: 872px; height: 440px;
    background:
      radial-gradient(circle at 82% 20%, rgba(60,20,10,0.7), transparent 18%),
      radial-gradient(circle at 12% 22%, rgba(200,90,50,0.7), transparent 20%),
      linear-gradient(180deg, #8a5a38 0%, #b07848 45%, rgba(230,180,120,0) 100%);
  }
  .brand {
    position: absolute; top: 146px; left: 0; width: 100%; text-align: center;
    font-family: "Archivo Black", Arial, sans-serif; font-weight: 400; font-size: 30px; letter-spacing: 1px;
    color: var(--brand);
  }
  .headline {
    position: absolute; top: 396px; left: 0; width: 100%; text-align: center;
    font-family: "Archivo Black", Arial, sans-serif; font-weight: 400; font-size: 64px; line-height: 80px;
    letter-spacing: -1px; color: var(--title); text-shadow: 0 2px 2px rgba(255,255,255,0.6);
  }
  .specials { position: absolute; left: 121px; top: 488px; width: 630px; }
  .special { margin-bottom: 5px; }
  .special__day {
    font-family: "Archivo Black", Arial, sans-serif; font-weight: 400; font-size: 24px; line-height: 28px;
    color: var(--amber); padding-left: 18px;
    text-shadow: 0 1px 2px rgba(0,0,0,0.6);
  }
  .special__panel {
    background: var(--panel); padding: 6px 22px 7px; box-shadow: 0 4px 10px rgba(0,0,0,0.5);
    color: var(--mint);
  }
  .special__title { font-size: 19px; letter-spacing: 0.5px; line-height: 22px; }
  .special__text { font-size: 14px; line-height: 17px; letter-spacing: 0.3px; }
  .price { color: var(--price); font-size: 17px; }
</style>
</head>
<body>
<main class="poster">
  <div class="hero-photo" role="img" aria-label="Foto: Hand am Billardqueue zwischen bunten Billardkugeln, mit leuchtenden Lichteffekten"></div>
  <div class="brand">KUGELWERK</div>
  <h1 class="headline">Wochenhighlights</h1>

  <section class="specials">
    <article class="special">
      <div class="special__day">Dienstag:</div>
      <div class="special__panel">
        <div class="special__title">Flatrate-Billard</div>
        <div class="special__text">Für nur <span class="price">5€ (7€)</span> pro Person den ganzen<br>Abend Pool-Billard (Snooker)spielen</div>
      </div>
    </article>
    <article class="special">
      <div class="special__day">Mittwoch:</div>
      <div class="special__panel">
        <div class="special__title">Studenten-Nacht</div>
        <div class="special__text">Studenten &amp; Auszubildende spielen<br>Pool-Billard für nur <span class="price">4,50€</span> die Stunde</div>
      </div>
    </article>
    <article class="special">
      <div class="special__day">Donnerstag:</div>
      <div class="special__panel">
        <div class="special__title">Snooker-Donnerstag</div>
        <div class="special__text">Donnerstags kostet der<br>Snooker Tisch gerade mal <span class="price">5€</span> die Stunde</div>
      </div>
    </article>
    <article class="special">
      <div class="special__day">Freitag:</div>
      <div class="special__panel">
        <div class="special__title">Kesselgold-Special</div>
        <div class="special__text">6 Talhof Kesselgold-Pils für nur <span class="price">11,99€</span></div>
      </div>
    </article>
    <article class="special">
      <div class="special__day">Samstag:</div>
      <div class="special__panel">
        <div class="special__title">Schau dein Wunschsspiel</div>
        <div class="special__text">Reserviere die Private Lounge und schaue das<br>Staffelrunde-Spiel deiner Wahl.<br>Reservierungsgebühr: <span class="price">10€</span>, ab 6 Personen kostenlos.<br>(Gilt auch für EP, VKT-Pokal &amp; Englische Wochen)</div>
      </div>
    </article>
    <article class="special">
      <div class="special__day">Sonntag:</div>
      <div class="special__panel">
        <div class="special__title">Play for Free</div>
        <div class="special__text">Wer vor 18:00 Uhr mit dem Spielen beginnt,<br>spielt den ganzen Abend umsonst!</div>
      </div>
    </article>
  </section>
</main>
</body>
</html>
```